Business Cards Needed

Hi designers, I have a new logo that was created by one of the ArtMingle designers. I'd now like to use that logo to make business cards. The company is called VitaLumen Advisors and is a business consulting firm. I'd like the business cards to be horizontal, modern, and professional.
I'd like the following information to be on the business card:
1) Logo
2) my name - Marisa Kolvane
3) my title - Principal
4) name of business - VitaLumen Advisors
5) mobile - 508.372.9146
6) e-mail - marisa@vitalumenadvisors.example
I'm uploading a JPG file of the logo. I'm hoping this is the correct file format. Please let me know if you need another type of file. Thank you.
Look and feel
Each slider illustrates characteristics of the customer's brand and the style your logo design should communicate.

```html
<!DOCTYPE html>
<html lang="en">
<head>
<meta charset="utf-8">
<title>VitaLumen Advisors – Business Card</title>
<link rel="stylesheet" href="https://fonts.googleapis.com/css2?family=Montserrat:wght@500;700&family=Lato:wght@400;700&display=swap">
<style>
  :root {
    --bg: #e9ebee;
    --card-green: #93c548;
    --card-white: #ffffff;
    --brand-blue: #1f6fbd;
    --brand-green: #8cc63f;
    --ink: #1d1d1f;
    --ink-soft: #3a3a3c;
    --shadow: 0 14px 34px rgba(0, 0, 0, 0.18);
  }
  * { box-sizing: border-box; margin: 0; padding: 0; }
  html, body { width: 1200px; height: 864px; overflow: hidden; }
  body {
    background: var(--bg);
    display: flex;
    align-items: center;
    justify-content: center;
    gap: 48px;
    font-family: "Lato", Arial, sans-serif;
  }
  .card {
    position: relative;
    width: 520px;
    height: 300px;
    border-radius: 22px;
    box-shadow: var(--shadow);
    overflow: hidden;
  }
  .card--front {
    background: var(--card-green);
    display: flex;
    align-items: center;
    justify-content: center;
  }
  .card--front .wordmark {
    font-family: "Montserrat", Arial, sans-serif;
    font-weight: 500;
    font-size: 40px;
    color: #ffffff;
    letter-spacing: 0.5px;
  }
  .card--back { background: var(--card-white); }
  .card--back .wordmark {
    position: absolute;
    left: 34px;
    top: 118px;
    font-family: "Montserrat", Arial, sans-serif;
    font-weight: 500;
    font-size: 26px;
    color: var(--brand-blue);
  }
  .name-tab {
    position: absolute;
    right: 0;
    top: 34px;
    width: 14px;
    height: 26px;
    background: var(--brand-green);
  }
  .identity {
    position: absolute;
    right: 34px;
    top: 34px;
    text-align: right;
  }
  .identity .person {
    font-family: "Montserrat", Arial, sans-serif;
    font-weight: 700;
    font-size: 21px;
    letter-spacing: 0.3px;
    line-height: 1.2;
  }
  .person .first { color: var(--brand-blue); }
  .person .last { color: var(--brand-green); }
  .identity .title {
    font-size: 13px;
    color: var(--ink-soft);
    margin-top: 2px;
  }
  .contact {
    position: absolute;
    left: 34px;
    bottom: 30px;
    list-style: none;
    font-size: 14px;
    color: var(--ink);
    line-height: 1.55;
  }
  .contact li { display: flex; align-items: center; gap: 8px; }
  .contact .company { font-size: 15px; }
  .contact svg { width: 13px; height: 13px; fill: var(--brand-green); flex: none; }
</style>
</head>
<body>
  <section class="card card--front">
    <span class="wordmark">VitaLumen Advisors</span>
  </section>

  <section class="card card--back">
    <span class="wordmark">VitaLumen Advisors</span>

    <span class="name-tab"></span>
    <div class="identity">
      <p class="person"><span class="first">MARISA</span> <span class="last">KOLVANE</span></p>
      <p class="title">Principal</p>
    </div>

    <ul class="contact">
      <li class="company">VitaLumen Advisors</li>
      <li>
        <svg viewBox="0 0 16 16" aria-hidden="true"><path d="M3.6 1.5l2.3 2.6-1.3 1.7c.9 2 2.5 3.6 4.6 4.6l1.7-1.3 2.6 2.3-1.5 2.1C6.8 13.2 2.8 9.2 1.5 3z"/></svg>
        <span>508.372.9146</span>
      </li>
      <li>
        <svg viewBox="0 0 16 16" aria-hidden="true"><path d="M1 3h14v10H1z M2 4.2v.4l6 4 6-4v-.4z" fill-rule="evenodd"/></svg>
        <span>marisa@vitalumenadvisors.example</span>
      </li>
    </ul>
  </section>
</body>
</html>
```